Beautiful Customer Appreciation Gift Box Need Eye Catching Brochure

I need a brochure to include with small sample gift boxes that I send or give to companies who do door to door marketing of businesses, company reps, real estate designers and large companies looking for a unique customer appreciation gifts.

The brochure needs to capture the size variations and the limitless options for their budget and customization needs.

They are gift boxes that can be filled with cookies for the drug rep making an impression for the doc - after cookies are gone, the gift remains

At christmas, we fill them with baked goods and provide to each office. Every year as i visit the offices, they have last years gift box out as a decoration.

realtors can use them as a welcome to your new home gift filled with a bottle of wine and their papers left on the kitchen counter

We have had them used for baby shower gifts, kept later as a decoration.

that's the concept, i need it captured.
Marlow's Festive Nook is the current name
a tag line we came up with is It's all in the WRAPPINGS.
Updates

Project Deadline Extended
Reason: We are very close, I have my photoshoot tomorrow and I'd like to see and continue to tweek the current designs. I have pretty well deleted the designs we are not considering at this point. The others all have components we love. So I need a little more time and some tweaking to decide for sure.

Target Market(s)

the target is the company or individuals looking for gift giving options for clients and customers. From the door to door salesperson looking to make a splash or big impression to the large company looking for nice corporate gift ideas.

The concept of say goodbye to plain jane gift boxes that all look alike... Say goodbye to expensive gift wrap and bows that get thrown away in minutes.... and hello to a beautiful custom made gift box that will remain a decoration or keepsake box forever....

Industry/Entity Type

Retail

Font styles to use
Sans Serif
Script

Requirements
Must have
• IMPORTANT... I CAN and AM GETTING better pictures for the printing purposes. I'm looking more for the concept of the brochuure and layout design.
• I'd love to have it have some place holders for various pictures and descriptions - because each industry targets different people, I'd like to be able to change the front cover of the brochure with a picture of a box that targets that audience a little.
• For a real estate person... i might choose a beautiful centerpiece looking one... vs, the ob/gyn office, I might choose a baby one.
• I have some design skill, just 0 times and the programs have changed alot over the years, so this may go on to future work and a long design relationship as the company grows and changes. I do know photoshop and pagemaker from long ago so I should be able to drop in pics and text options. if we use compatible programs.
Nice to have
• would love to have some kind of background for the page - not just plain white background.
• i like angles and curves
Should not have
• boxy look.

```html
<!DOCTYPE html>
<html lang="en">
<head>
<meta charset="UTF-8">
<title>Trifold Brochure – Inside Spread</title>
<link rel="stylesheet" href="https://fonts.googleapis.com/css2?family=Montserrat:wght@400;600;800&display=swap">
<style>
  :root {
    --page-bg: #e6e6e6;
    --cream: #fbe5bd;
    --cream-deep: #f4d3a0;
    --lilac: #caa0d0;
    --lilac-soft: #dcbfe0;
    --plum: #9b4f9d;
    --plum-deep: #6a1f6d;
    --mauve: #b57a95;
    --orchid: #b67cbb;
    --white: #ffffff;
    --body-plum: #8b3a8d;
  }
  * { box-sizing: border-box; margin: 0; padding: 0; }
  html, body { width: 1200px; height: 800px; overflow: hidden; }
  body {
    background: var(--page-bg);
    font-family: "Montserrat", Arial, sans-serif;
    position: relative;
  }
  .brochure {
    position: absolute;
    left: 75px; top: 80px;
    width: 1050px; height: 640px;
    background: linear-gradient(180deg, var(--cream) 0%, var(--cream-deep) 100%);
    box-shadow: 0 18px 40px rgba(0,0,0,0.22);
    overflow: hidden;
  }
  .brochure__art { position: absolute; inset: 0; }
  .photo { position: absolute; display: block; }
  .photo--arrangement-pink { left: 70px; top: 60px; }
  .photo--arrangement-blue { left: 425px; top: 70px; }
  .photo--arrangement-violet { left: 770px; top: 18px; }
  .photo--box-small { left: 556px; top: 344px; }
  .photo--box-large { left: 700px; top: 330px; }

  .product {
    position: absolute;
    width: 250px;
  }
  .product--one { left: 95px; top: 318px; }
  .product--two { left: 405px; top: 275px; }
  .product--three { left: 745px; top: 205px; }
  .product__title {
    color: var(--plum-deep);
    font-weight: 800;
    font-size: 14px;
    line-height: 1.1;
    text-transform: uppercase;
    letter-spacing: 0.2px;
  }
  .product__text {
    margin-top: 5px;
    color: var(--body-plum);
    font-size: 9.5px;
    line-height: 1.3;
  }

  .budget {
    position: absolute;
    left: 120px; top: 505px;
    width: 250px;
    color: var(--white);
  }
  .budget__title {
    font-weight: 800;
    font-size: 15px;
    line-height: 1.15;
    text-transform: uppercase;
  }
  .budget__text {
    margin-top: 6px;
    font-size: 9.5px;
    line-height: 1.3;
  }
  .budget__text + .budget__text { margin-top: 9px; }

  .details {
    position: absolute;
    left: 405px; top: 508px;
    width: 200px;
    color: var(--white);
    font-size: 9.5px;
    line-height: 1.3;
  }
</style>
</head>
<body>
  <main class="brochure">
    <svg class="brochure__art" width="1050" height="640" viewBox="0 0 1050 640" aria-hidden="true">
      <defs>
        <linearGradient id="bandTop" x1="0" y1="0" x2="1" y2="0">
          <stop offset="0" stop-color="#c898cf"/>
          <stop offset="1" stop-color="#d9b8de"/>
        </linearGradient>
        <linearGradient id="bandBottom" x1="0" y1="0" x2="0" y2="1">
          <stop offset="0" stop-color="#bd86c0"/>
          <stop offset="1" stop-color="#a867ad"/>
        </linearGradient>
      </defs>
      <path d="M0,0 H1050 V70 C880,50 760,40 620,95 C470,150 260,120 0,150 Z" fill="var(--mauve)"/>
      <path d="M0,0 H1050 V55 C880,35 760,25 620,80 C470,135 260,105 0,128 Z" fill="var(--plum)"/>
      <path d="M0,0 H1050 V40 C880,22 760,12 620,64 C470,118 260,90 0,110 Z" fill="url(#bandTop)"/>
      <path d="M350,0 C520,40 700,30 1050,0 V18 C760,45 560,60 350,20 Z" fill="var(--lilac-soft)" opacity="0.6"/>
      <path d="M0,470 C180,440 380,455 560,470 C640,476 690,470 720,462 L720,640 H0 Z" fill="url(#bandBottom)"/>
      <path d="M0,455 C190,420 380,440 560,452 C640,458 690,452 720,444 L720,462 C690,470 640,476 560,470 C380,455 180,440 0,470 Z" fill="var(--plum)"/>
      <path d="M0,488 C120,462 240,448 380,452 C300,462 170,480 0,518 Z" fill="var(--white)"/>
      <path d="M380,468 C470,452 560,446 660,444 C570,454 480,466 392,488 Z" fill="var(--white)"/>
      <line x1="350" y1="0" x2="350" y2="640" stroke="#000" stroke-opacity="0.06" stroke-width="2"/>
      <line x1="700" y1="0" x2="700" y2="640" stroke="#000" stroke-opacity="0.06" stroke-width="2"/>
    </svg>

    <svg class="photo photo--arrangement-pink" width="210" height="200" viewBox="-5 -5 210 200" role="img" aria-label="Photo: pink rose arrangement on a decorated gift box">
      <defs><linearGradient id="pinkFill" x1="0" y1="0" x2="0" y2="1"><stop offset="0" stop-color="#8a6a5a"/><stop offset="0.5" stop-color="#e4a9bf"/><stop offset="1" stop-color="#d99ab3"/></linearGradient></defs>
      <path d="M20,0 H180 Q180,20 200,20 V170 Q180,170 180,190 H20 Q20,170 0,170 V20 Q20,20 20,0 Z" fill="url(#pinkFill)" stroke="var(--white)" stroke-width="6"/>
    </svg>

    <svg class="photo photo--arrangement-blue" width="210" height="185" viewBox="-5 -5 210 185" role="img" aria-label="Photo: blue and cream silk flower arrangement">
      <defs><linearGradient id="blueFill" x1="0" y1="0" x2="1" y2="1"><stop offset="0" stop-color="#5a4a3a"/><stop offset="0.5" stop-color="#6f8fb8"/><stop offset="1" stop-color="#7c6650"/></linearGradient></defs>
      <path d="M20,0 H180 Q180,20 200,20 V155 Q180,155 180,175 H20 Q20,155 0,155 V20 Q20,20 20,0 Z" fill="url(#blueFill)" stroke="var(--white)" stroke-width="6"/>
    </svg>

    <svg class="photo photo--arrangement-violet" width="200" height="180" viewBox="-5 -5 200 180" role="img" aria-label="Photo: violet and white floral centerpiece box">
      <defs><linearGradient id="violetFill" x1="0" y1="0" x2="0" y2="1"><stop offset="0" stop-color="#7a6a58"/><stop offset="0.5" stop-color="#8e7bc8"/><stop offset="1" stop-color="#4f5a3a"/></linearGradient></defs>
      <path d="M20,0 H170 Q170,20 190,20 V150 Q170,150 170,170 H20 Q20,150 0,150 V20 Q20,20 20,0 Z" fill="url(#violetFill)" stroke="var(--white)" stroke-width="6"/>
    </svg>

    <svg class="photo photo--box-small" width="150" height="150" viewBox="0 0 150 150" role="img" aria-label="Photo: small open keepsake gift box">
      <defs><radialGradient id="smallFill"><stop offset="0" stop-color="#a88a5c"/><stop offset="1" stop-color="#4a3a5c"/></radialGradient></defs>
      <circle cx="75" cy="75" r="66" fill="url(#smallFill)" stroke="var(--white)" stroke-width="6"/>
      <circle cx="75" cy="75" r="70" fill="none" stroke="var(--plum-deep)" stroke-width="3"/>
    </svg>

    <svg class="photo photo--box-large" width="350" height="310" viewBox="0 0 350 310" role="img" aria-label="Photo: large book-style keepsake box with greenery on a wooden table">
      <defs><linearGradient id="largeFill" x1="0" y1="0" x2="1" y2="1"><stop offset="0" stop-color="#6a4a2c"/><stop offset="0.5" stop-color="#c9b27a"/><stop offset="1" stop-color="#3a2a1c"/></linearGradient></defs>
      <path d="M70,40 Q130,0 210,12 L350,0 V310 H10 Q30,260 20,200 Q40,110 70,40 Z" fill="url(#largeFill)" stroke="var(--white)" stroke-width="6"/>
    </svg>

    <section class="product product--one">
      <h2 class="product__title">Price<br>Product Description</h2>
      <p class="product__text">Lorem ipsum dolor sit amet, consectetur adipiscing elit, sed do eiusmod tempor incididunt ut labore et dolore magna aliqua.</p>
    </section>

    <section class="product product--two">
      <h2 class="product__title">Price<br>Product Description</h2>
      <p class="product__text">Lorem ipsum dolor sit amet, consectetur adipiscing elit, sed do eiusmod tempor incididunt ut labore et dolore magna aliqua.</p>
    </section>

    <section class="product product--three">
      <h2 class="product__title">Price<br>Product Description</h2>
      <p class="product__text">Lorem ipsum dolor sit amet, consectetur adipiscing elit, sed do eiusmod tempor incididunt ut labore et dolore magna aliqua.</p>
    </section>

    <section class="budget">
      <h2 class="budget__title">What your<br>budget can get you</h2>
      <p class="budget__text">Lorem ipsum dolor sit amet, consectetur adipiscing elit, sed do eiusmod tempor incididunt ut labore et dolore magna aliqua.</p>
      <p class="budget__text">Lorem ipsum dolor sit amet, consectetur adipiscing elit, sed do eiusmod tempor incididunt ut labore et dolore magna aliqua.</p>
    </section>

    <p class="details">Lorem ipsum dolor sit amet, consectetur adipiscing elit, sed do eiusmod tempor incididunt ut labore et dolore magna aliqua. Lorem ipsum dolor sit amet, consectetur adipiscing elit, sed do eiusmod tempor incididunt ut labore et dolore magna aliqua.</p>
  </main>
</body>
</html>
```